3 back Windows only wrapped for world’s smallest cargo van – midget -purple

Needed to update and clarify the description.
*Seeking award-winning graphic designer with expertise in vintage typography and vehicle branding*

**Project Overview**
Design a cohesive, high-impact vinyl wrap series for the three rear windows of a cargo van (passenger, driver, and rear). The design must convey **vintage elegance with a bold personality**, blending classical aesthetics feel with modern creative artistry. This is not a full vehicle wrap—only the three rear windows will be wrapped.

**Key Requirements**
- Three separate but visually unified designs, one for each window:
- Passenger window: 32" x 21"
- Driver window: 32.5" x 21.25"
- Rear window: 39.5" x 17.75"
- The **logo (provided)** must appear in **each window**, centrally or compositionally anchored.
- The **law firm name** must appear in **each window**, but **not necessarily adjacent to the logo**—placement should serve the overall design.
- The **phone number (713) 555-0148** must be clearly visible and included on **all three windows**.

**Design Direction**
- **Style**: Vintage with a bold personality. Think *classic hand-crafted signwriting*—inspired by **hand-lettered serifs and brush scripts**, but not imitative.
- **Tone**: Professional, authoritative, and distinctive. The vehicle should command attention as a mobile representation of elevated justice.
- **Creative Concept**: Incorporate a stylized, proprietary interpretation of **Lady Justice**, reimagined with **one hand raised higher than the other**, symbolizing that clients receive *higher justice*. This element should be subtle, artistic, and integrated into the background or border—**not literal or cliché**.
- **No traditional legal symbols** (e.g., scales, gavels, pillars) beyond those in the provided assets.
- **Color Palette**: Derived from the brand’s existing logo and reference images (designer to extract and harmonize). Must feel rich, timeless, and legible.
- **Typography**:
- Use the **existing font for the law office name** (from the logo) as a base.
- All other typography (phone, decorative text, etc.) may be experimental—**hand-drawn, brush script, or vintage serif styles encouraged**.

• The logo, company name, phone number, artistic input, BE CREATIVE!
• Nice to have one of these slogans: 1) Holding insurance companies accountable, When they refuse to be responsible. OR 2) The storm has its harbor. Fairness has its Keeper. The Fairness Keeper.
• The look of a business card. BORING

```html
<!DOCTYPE html>
<html lang="en">
<head>
<meta charset="utf-8">
<title>Corvin Law – Rear Window Wraps</title>
<link href="https://fonts.googleapis.com/css2?family=Marcellus&family=Tinos:wght@700&display=swap" rel="stylesheet">
<style>
  :root {
    --canvas: #e1e1e1;
    --panel-dark: #2a1415;
    --panel-dark-deep: #1d0d0e;
    --ray-light: #3a2223;
    --copper: #f2a583;
    --copper-light: #f7b899;
    --copper-deep: #c76a4a;
    --ink: #241012;
  }
  html, body {
    margin: 0;
    padding: 0;
    width: 1200px;
    height: 2873px;
    overflow: hidden;
    background: var(--canvas);
  }
  .wrap-sheet {
    width: 1200px;
    height: 2873px;
    display: flex;
    flex-direction: column;
    align-items: center;
    justify-content: space-evenly;
  }
  .window-panel {
    display: block;
    width: 1040px;
    box-shadow: 0 4px 10px rgba(0,0,0,0.35);
  }
  .window-panel--rear { height: 575px; }
  .window-panel--side { height: 700px; }
  .firm-name {
    font-family: "Marcellus", serif;
    fill: var(--copper);
  }
  .firm-tagline {
    font-family: "Marcellus", serif;
    fill: var(--copper);
    letter-spacing: 0.08em;
  }
  .firm-mark { fill: var(--copper); }
  .phone-number {
    font-family: "Tinos", serif;
    font-weight: 700;
    fill: var(--ink);
  }
  .wave-copper { fill: url(#copperSheen); }
  .wave-edge { fill: var(--copper-light); }
  .stop-ray-center { stop-color: var(--ray-light); }
  .stop-ray-outer { stop-color: var(--panel-dark-deep); }
  .stop-copper-a { stop-color: var(--copper); }
  .stop-copper-b { stop-color: var(--copper-deep); }
  .stop-copper-c { stop-color: var(--copper-light); }
</style>
</head>
<body>
<main class="wrap-sheet">

  <svg width="0" height="0" style="position:absolute" aria-hidden="true">
    <defs>
      <radialGradient id="rayGlow" cx="0.4" cy="0.4" r="0.8">
        <stop offset="0" class="stop-ray-center"/>
        <stop offset="1" class="stop-ray-outer"/>
      </radialGradient>
      <linearGradient id="copperSheen" x1="0" y1="0" x2="1" y2="1">
        <stop offset="0" class="stop-copper-a"/>
        <stop offset="0.55" class="stop-copper-b"/>
        <stop offset="1" class="stop-copper-c"/>
      </linearGradient>
    </defs>
  </svg>

  <!-- Rear window -->
  <svg class="window-panel window-panel--rear" viewBox="0 0 715 395" preserveAspectRatio="none">
    <g role="img" aria-label="Dark sunburst rays radiating behind the firm name">
      <rect width="715" height="395" fill="url(#rayGlow)"/>
    </g>
    <path class="wave-edge" d="M0,318 C80,238 200,233 350,228 C500,223 650,218 715,158 L715,170 C650,230 500,235 350,240 C200,245 80,250 0,330Z"/>
    <path class="wave-copper" d="M0,330 C80,250 200,245 350,240 C500,235 650,230 715,170 L715,395 L0,395Z"/>
    <circle class="firm-mark" cx="250" cy="128" r="20"/>
    <text class="firm-name" x="288" y="147" font-size="54">CORVIN LAW</text>
    <text class="firm-tagline" x="350" y="178" font-size="16">PERSONAL INJURY LAW FIRM</text>
    <text class="phone-number" x="357" y="335" font-size="58" text-anchor="middle">(713) 555-0148</text>
  </svg>

  <!-- Passenger window -->
  <svg class="window-panel window-panel--side" viewBox="0 0 310 240" preserveAspectRatio="none">
    <g role="img" aria-label="Dark sunburst rays radiating behind the firm name">
      <rect width="310" height="240" fill="url(#rayGlow)"/>
    </g>
    <path class="wave-edge" d="M0,184 C40,144 120,144 200,139 C260,134 300,119 310,99 L310,105 C300,125 260,140 200,145 C120,150 40,150 0,190Z"/>
    <path class="wave-copper" d="M0,190 C40,150 120,150 200,145 C260,140 300,125 310,105 L310,240 L0,240Z"/>
    <circle class="firm-mark" cx="82" cy="82" r="10"/>
    <text class="firm-name" x="100" y="92" font-size="26">CORVIN LAW</text>
    <text class="firm-tagline" x="118" y="106" font-size="7.5">PERSONAL INJURY LAW FIRM</text>
    <text class="phone-number" x="155" y="198" font-size="30" text-anchor="middle">(713) 555-0148</text>
  </svg>

  <!-- Driver window -->
  <svg class="window-panel window-panel--side" viewBox="0 0 367 240" preserveAspectRatio="none">
    <g role="img" aria-label="Dark sunburst rays radiating behind the firm name">
      <rect width="367" height="240" fill="url(#rayGlow)"/>
    </g>
    <path class="wave-edge" d="M0,97 C40,142 150,142 250,157 C312,167 334,204 346,240 L340,240 C330,210 310,175 250,165 C150,150 40,150 0,105Z"/>
    <path class="wave-copper" d="M0,105 C40,150 150,150 250,165 C310,175 330,210 340,240 L0,240Z"/>
    <circle class="firm-mark" cx="104" cy="90" r="10"/>
    <text class="firm-name" x="122" y="100" font-size="26">CORVIN LAW</text>
    <text class="firm-tagline" x="142" y="114" font-size="7.5">PERSONAL INJURY LAW FIRM</text>
    <text class="phone-number" x="150" y="208" font-size="30" text-anchor="middle">(713) 555-0148</text>
  </svg>

</main>
</body>
</html>
```